The Funding of Orphanage Home

A4 size flyer, 2 pages, Color.

We provide the word contents(Chinese and English), related pictures(designer select for use), logo and a direction map to our orphanage home.

```html
<!DOCTYPE html>
<html lang="zh">
<head>
<meta charset="utf-8">
<title>We Need Your Help</title>
<link rel="stylesheet" href="https://fonts.googleapis.com/css2?family=Noto+Sans+SC:wght@400;500;700;900&family=Oswald:wght@400;500;700&display=swap">
<style>
:root{
  --red:#d7262e;
  --deep:#b3121b;
  --ink:#2a2a2a;
  --soft:#f6e3e1;
  --rose:#e9b9b6;
  --line:#9a9a9a;
}
*{box-sizing:border-box;margin:0;padding:0}
html,body{width:849px;height:1200px;overflow:hidden;background:#fff}
body{font-family:"Noto Sans SC",sans-serif;color:var(--ink);position:relative}
.abs{position:absolute}
.title-cn{left:40px;top:30px;font-size:27px;font-weight:500;letter-spacing:2px;color:#333}
.title-en{left:38px;top:64px;font-family:"Oswald",sans-serif;font-weight:700;font-size:40px;color:var(--red);letter-spacing:1px}
.brand{right:40px;top:24px;display:flex;flex-direction:column;align-items:center;gap:4px}
.brand .dot{width:60px;height:60px;border-radius:50%;background:var(--red)}
.brand span{font-size:11px;font-weight:700;color:var(--red)}
.sec-head{font-size:19px;font-weight:700;color:var(--red);border-bottom:2px solid var(--red);padding-bottom:3px;display:flex;gap:10px;align-items:baseline}
.sec-head b{font-family:"Oswald",sans-serif;font-weight:500;font-size:19px}
.list{list-style:none;font-size:11px;line-height:21px;color:#333}
.list li{display:flex;align-items:center;gap:6px}
.list li::before{content:"";width:10px;height:10px;border:1px solid #666;flex:none}
.list .tall{line-height:13px;align-items:flex-start}
.list .tall::before{margin-top:2px}
.band{left:40px;right:40px;top:388px;display:flex;align-items:center;gap:14px;font-size:19px;font-weight:700;color:var(--red)}
.band::before,.band::after{content:"";flex:1;height:2px;background:var(--red)}
.band b{font-family:"Oswald",sans-serif;font-weight:500}
.fin-head{font-size:14px;font-weight:700;color:#222;border-bottom:1px solid var(--red);padding-bottom:2px}
.fin-head b{font-family:"Oswald",sans-serif;font-weight:500}
.amt{color:var(--red);font-weight:700;margin-left:6px}
.lower{left:0;top:560px;width:849px;height:640px;background:linear-gradient(180deg,#fff 0%,var(--soft) 35%,var(--soft) 100%)}
.map{left:40px;top:610px;width:330px;height:300px;background:#f3f0ec;border:1px solid #ddd}
.stamp{left:32px;top:640px;width:140px;height:140px;border-radius:50%;background:var(--red);color:#fff;display:flex;flex-direction:column;align-items:center;justify-content:center;text-align:center;line-height:1.15}
.stamp .here{font-family:"Oswald",sans-serif;font-size:18px;color:#ffe14a}
.stamp .cn{font-size:22px;font-weight:900}
.stamp .en{font-family:"Oswald",sans-serif;font-size:11px;letter-spacing:1px}
.photos{left:0;top:930px;width:400px;height:270px;background:linear-gradient(135deg,#c9a897,#e7c9c2 55%,#b5827a)}
.form-head{left:422px;top:662px;width:390px;height:34px;background:var(--red);color:#fff;font-size:20px;font-weight:700;display:flex;align-items:center;gap:10px;padding-left:12px}
.form-head b{font-family:"Oswald",sans-serif;font-weight:500}
.form{left:426px;top:706px;width:386px;list-style:none}
.form li{height:26px;display:flex;align-items:flex-end;font-size:11px;color:#333;padding-bottom:3px}
.form li span{white-space:nowrap;margin-right:6px}
.form li::after{content:"";flex:1;border-bottom:1px dotted #555;margin-bottom:3px}
.form li.blank::after{margin-left:0}
</style>
</head>
<body>
<div class="abs title-cn">我们需要您的协助</div>
<div class="abs title-en">WE NEED YOUR HELP</div>
<div class="abs brand"><div class="dot"></div><span>Rumah Kasih</span></div>

<section class="abs" style="left:40px;top:140px;width:370px">
  <div class="sec-head">老师 <b>TEACHER</b></div>
  <div style="display:flex;gap:24px;margin-top:8px">
    <ul class="list" style="width:160px">
      <li>英语English</li><li>国语 Malaysia</li><li>电脑Computer</li><li>美术/手工 Art</li><li>佛学班 Dharma Class</li><li>音乐 Music</li>
    </ul>
    <ul class="list">
      <li>华语 Chinese</li><li>数学 Mathematics</li><li>康乐活动 Recreation Activity</li><li>戏剧 Drama</li><li class="tall">注册心理辅导 Registered<br>Psychological Counseling</li>
    </ul>
  </div>
</section>

<section class="abs" style="left:440px;top:140px;width:370px">
  <div class="sec-head">医疗饮食 <b>MEDICAL DIETARY</b></div>
  <div style="display:flex;gap:24px;margin-top:8px">
    <ul class="list" style="width:160px"><li>西医 Western Medicine</li><li>中医 Chinese Medicine</li></ul>
    <ul class="list"><li>素食烹饪 Vegetarian Cuisine</li><li>营养师 Nutritionist</li></ul>
  </div>
  <div class="sec-head" style="margin-top:18px">技术人员 <b>TECHNICIAN</b></div>
  <div style="display:flex;gap:24px;margin-top:8px">
    <ul class="list" style="width:160px"><li>水喉Plumbing</li><li>园艺 Gardening</li></ul>
    <ul class="list"><li>电工 Electrician</li><li>土木 Construction</li></ul>
  </div>
</section>

<div class="abs band">寻找经济资源 <b>FINANCIAL RESOURCES</b></div>

<section class="abs" style="left:40px;top:424px;width:360px">
  <div class="fin-head">孤儿院 <b>ORPHANAGE HOME</b></div>
  <ul class="list" style="margin-top:4px">
    <li>电费 Electricity<span class="amt">RM 1200/月/mth</span></li>
    <li>水费 Water<span class="amt">RM 400/月/mth</span></li>
    <li>电话费 Phone<span class="amt">RM 300/月/mth</span></li>
    <li>发展基金 Development Fund : RM ____________</li>
  </ul>
</section>
<section class="abs" style="left:440px;top:424px;width:370px">
  <div class="fin-head">孩子每月费用 <b>MONTHLY EXPENSES/CHILD</b></div>
  <ul class="list" style="margin-top:4px">
    <li>伙食费 Meals<span class="amt">RM 300/月/mth</span></li>
    <li>学费 School Fee<span class="amt">RM 150/月/mth</span></li>
    <li>巴士费 Bus Fare<span class="amt">RM 80/月/mth</span></li>
    <li>零用钱 Pocket Money<span class="amt">RM 50/月/mth</span></li>
    <li>教育基金 Education Fund : RM ____________</li>
  </ul>
</section>

<div class="abs lower"></div>
<div class="abs map" role="img" aria-label="Direction map to the children's home"></div>
<div class="abs stamp"><span class="here">We're Here!</span><span class="en">RUMAH KASIH</span><span class="cn">慈心儿童之家</span><span class="en">CHILDREN'S HOME</span></div>
<div class="abs photos" role="img" aria-label="Photos of children at the home"></div>

<div class="abs form-head">个人资料 <b>PERSONAL DETAILS</b></div>
<ul class="abs form">
  <li><span>姓名 Name</span></li>
  <li><span>身份证号码 I/C No.</span></li>
  <li><span>出生日期 Date of Birth</span></li>
  <li><span>性别 Sex</span></li>
  <li><span>宗教 Religion</span></li>
  <li><span>国籍Nationality</span></li>
  <li><span>婚姻状况Marital Status</span></li>
  <li><span>地址 Address</span></li>
  <li class="blank"></li>
  <li><span>职业 Occupation</span></li>
  <li><span>手提电话 H/P No.</span></li>
  <li><span>住家/公司电话 Tel.</span></li>
  <li><span>电邮 Email Address</span></li>
</ul>
</body>
</html>
```